Mirrorglow 90's Revival club night

I am after either an A5 or DL flyer but also the formats for using the design on social media etc.
The flyer is for a 90's revival club night at a nightclub that was well attended in the 90's . A special guest PA - Honey Q famous for her single 'Carry me through the starlight' ,is performing.
I have a logo for the night that may have to be altered / edited to fit in with your design (Colours changed etc) but also have a logo for the artist that may be more restrictive in regards to any changes.Both are attached.
Look forward to hearing from you shortly,

Tam

Reason: Required text to go on the flyer has now be added to the brief. Majority of designs submitted didn't seem to reflect to '90's nightclub' feel we were hoping for. Most of the designs used the colour scheme based on the 'Mirrorglow' logo. We are hoping that these colours can be ignored with some designs and that the logo is made of of different colours that would make it easier for it to fit in with the designers ideas. Regards Tam

Target Market(s)

20 to 50 years age range who use to go clubbing / still do / love the 90's music. Club that they use to attend in the 90's is where the event is being held

Industry/Entity Type

Club

Requirements
Must have
• Both the logos for the event ( Mirrorglow 90's Revival and Honey Q ) must be included on the flyer. Colours and the format can be altered on the mirrorglow logo but the design should remain as close to the original as sent. 90's font and images would also be a must if possible. Honey Q logo can have colors altered, but not the font or design.
• Text required as follows :
• Venue : Club Orbit, Pellingford Lane, Westbury, Wiltshire
• Date : Saturday 10th June 2017
• Time : 8.30pm till 3am
• Very special guest PA ‘ HONEY Q’ ‘Carry me through the starlight’
• DJ’s : Main room – Danny Holtsby ( Arcade 77 / Mirrorglow )
• Room 2 – Simon P
• Full club décor with Laser lightshow, CO’2 cannons and pryrotechnics
• Tickets : £15 VIP / £10 General Admission – Available from : https://www.passgate-example.co.uk/venue/QZTRWN
• Or ‘Club Orbit’ : 01632 960418
• Web : www.ravebackclub-example.co.uk
Nice to have
• open to ideas
Should not have
• Not to cheesy ........

```html
<!DOCTYPE html>
<html lang="en">
<head>
<meta charset="utf-8">
<title>Mirrorglow 90's Revival – Club Orbit</title>
<link rel="stylesheet" href="https://fonts.googleapis.com/css2?family=Archivo+Black&family=Russo+One&family=Asap+Condensed:wght@600;700&family=Alegreya+Sans+SC:wght@500;700&display=swap">
<style>
  :root {
    --yellow: #f6e71d;
    --aqua: #5fd6e8;
    --ice: #8fd9dc;
    --ink: #111111;
    --white: #ffffff;
    --grey-box: rgba(120,130,130,0.85);
    --navy: #1d5f9e;
  }
  * { margin: 0; padding: 0; box-sizing: border-box; }
  html, body { width: 855px; height: 1200px; overflow: hidden; background: var(--white); }
  .flyer {
    position: relative; width: 855px; height: 1200px; overflow: hidden;
    font-family: "Asap Condensed", sans-serif;
  }
  .backdrop {
    position: absolute; inset: 0;
    background:
      radial-gradient(ellipse 38% 55% at 50% 62%, rgba(40,70,40,0.55), transparent 70%),
      radial-gradient(circle at 20% 30%, #5fb3b0 0, transparent 45%),
      linear-gradient(160deg, #4fa9a6 0%, #2f7d78 40%, #3d6b3e 70%, #2d8a88 100%);
  }
  .band { position: absolute; background: var(--yellow); color: var(--ink); }
  .presents {
    left: 0; right: 0; top: 62px; height: 46px;
    font-family: "Archivo Black", sans-serif; font-size: 33px;
    text-align: center; line-height: 46px; letter-spacing: 0.5px;
  }
  .event-mark {
    position: absolute; left: 40px; top: 150px; width: 300px;
    color: var(--yellow); font-family: "Asap Condensed", sans-serif; font-weight: 700;
    display: flex; align-items: center; gap: 12px;
  }
  .event-mark .dot { width: 26px; height: 26px; border-radius: 50%; background: var(--yellow); flex: none; }
  .event-mark .name { font-size: 48px; line-height: 1; }
  .event-mark .sub { font-size: 30px; line-height: 1.1; display: block; }
  .best-badge {
    position: absolute; left: 645px; top: 125px; width: 228px; height: 228px;
    border-radius: 50%; background: var(--yellow); color: var(--ink);
    font-family: "Archivo Black", sans-serif; text-align: center;
    display: flex; flex-direction: column; justify-content: center;
  }
  .best-badge .small { font-size: 19px; line-height: 1.05; }
  .best-badge .big { font-family: "Asap Condensed", sans-serif; font-weight: 700; font-size: 92px; line-height: 0.95; letter-spacing: -2px; }
  .venue-band {
    position: absolute; left: 0; right: 0; top: 363px; height: 122px;
    background: var(--white); display: flex; align-items: center; justify-content: center;
  }
  .venue-name {
    font-family: "Russo One", sans-serif; font-size: 100px; color: var(--ice);
    letter-spacing: 2px; text-shadow: 4px 4px 0 #1b3a3a; font-weight: 400;
  }
  .date-box {
    position: absolute; left: 59px; top: 520px; width: 372px; height: 92px;
    background: var(--grey-box); color: var(--yellow);
    padding: 6px 8px; font-weight: 700;
  }
  .date-box .date, .date-box .time { font-size: 24px; line-height: 28px; }
  .date-box .address { font-size: 17px; line-height: 26px; }
  .dj-heading, .dj-line {
    font-family: "Alegreya Sans SC", sans-serif; font-weight: 500;
    white-space: nowrap; padding: 0 8px;
    transform: translateX(-50%);
  }
  .dj-heading { left: 622px; top: 604px; height: 36px; font-size: 28px; line-height: 36px; }
  .dj-main { left: 427px; top: 656px; height: 40px; font-size: 29px; line-height: 40px; }
  .dj-second { left: 436px; top: 710px; height: 40px; font-size: 29px; line-height: 40px; }
  .guest-band {
    position: absolute; left: 73px; top: 772px; width: 758px; height: 54px;
    background: var(--aqua); color: var(--yellow);
    font-family: "Alegreya Sans SC", sans-serif; font-weight: 700;
    font-size: 25px; line-height: 54px; text-align: center; white-space: nowrap;
  }
  .guest-band .artist { color: var(--navy); }
  .artist-mark {
    position: absolute; left: 0; right: 0; top: 838px; text-align: center;
    font-family: "Russo One", sans-serif; font-size: 104px; color: var(--white); line-height: 1.1;
  }
  .label-mark {
    position: absolute; left: 0; right: 0; top: 958px; text-align: center;
    font-family: "Asap Condensed", sans-serif; font-weight: 700; font-size: 14px; color: var(--white);
    letter-spacing: 1px;
  }
  .info-line {
    position: absolute; left: 0; background: var(--white); color: var(--ink);
    font-family: "Alegreya Sans SC", sans-serif; font-weight: 700;
    font-size: 25px; padding: 0 8px; white-space: nowrap;
  }
  .info-decor { top: 1029px; height: 32px; line-height: 32px; }
  .info-tickets { top: 1067px; height: 32px; line-height: 32px; }
  .info-source { top: 1105px; height: 32px; line-height: 32px; }
  .info-phone { top: 1146px; height: 30px; line-height: 30px; font-size: 19px; }
  .web-line {
    position: absolute; right: 0; top: 1146px; height: 30px; line-height: 30px;
    background: var(--white); color: var(--ink); padding: 0 10px;
    font-family: "Alegreya Sans SC", sans-serif; font-weight: 700; font-size: 19px;
  }
</style>
</head>
<body>
<main class="flyer">
  <div class="backdrop" role="img" aria-label="Teal grunge backdrop with paint splatters and a faint silhouette of a dancing woman"></div>

  <div class="band presents">OUR NIGHTCLUB PROMOTION PRESENTS</div>

  <div class="event-mark">
    <span class="dot"></span>
    <span><span class="name">Mirrorglow</span><span class="sub">90's Revival</span></span>
  </div>

  <div class="best-badge">
    <span class="small">ONLY<br>THE BEST</span>
    <span class="big">90's</span>
    <span class="small">MUSIC IN<br>TOWN</span>
  </div>

  <div class="venue-band"><h1 class="venue-name">CLUB ORBIT</h1></div>

  <div class="date-box">
    <div class="date">SATURDAY 10TH JUNE '17</div>
    <div class="time">8.30pm till 3.00am</div>
    <div class="address">Pellingford Lane, Westbury, Wiltshire</div>
  </div>

  <div class="band dj-heading">DJ's</div>
  <div class="band dj-line dj-main">Danny Holtsby - Main room ( Arcade 77 / Mirrorglow )</div>
  <div class="band dj-line dj-second">Simon P - Room 2</div>

  <div class="guest-band">Very special guest <span class="artist">PA ' HONEY Q</span> "Carry me through the starlight"</div>

  <div class="artist-mark">Honey Q</div>
  <div class="label-mark">KESTREL PROD</div>

  <div class="info-line info-decor">Full club décor with Laser lightshow, CO'2 cannons and pyrotechnics</div>
  <div class="info-line info-tickets">Tickets : £15 VIP / £10 General Admission</div>
  <div class="info-line info-source">Available from : www.passgate-example.co.uk/venue/QZTRWN</div>
  <div class="info-line info-phone">Or 'Club Orbit' : 01632 960418</div>
  <div class="web-line">www.ravebackclub-example.co.uk</div>
</main>
</body>
</html>
```